Energieberater sucht Flyer-Design
Zielgruppe
Ich bin Energieberater, habe mich vor kurzem selbstständig gemacht und möchte nun meine Bekanntheit steigern. Meine Zielgruppe sind Immobilieneigentümer sowie Immobiliensuchende, welchen ich eine fundierte Energieberatung mit Sanierungskonzepten sowie die Erstellung von Energieausweisen bieten kann.
Aufgabenstellung
Ich benötige einen Flyer, welchen ich regional verteilen möchte. Der Flyer soll quadratisch (148 x 148) erstellt werden.
Der Flyer sollte mein Logo, meine Kontaktdaten, die unten aufgeführten Dienstleistungen sowie einen Gutschein enthalten und insbesondere der Bekanntheits-/Imagesteigerung dienen.
Vorhandene Punkte sollen sein:
- Erstellung von Energieausweisen für Vermietung und Verkauf
- Energieberatung
- Sanierungs- und Modernisierungskonzepte
- Fördermittelberatung
Der Flyer soll die Möglichkeit bieten, am Rand abgeschnitten zu werden. Dort soll ein Gutschein aufgeführt werden mit 25 € Rabatt für einen Energieausweis.
Meine Kontaktdaten können Sie der angehängten Visitenkarte entnehmen.

```html
<!DOCTYPE html>
<html lang="de">
<head>
<meta charset="utf-8">
<title>Flyer Energieberatung Wendler</title>
<link rel="stylesheet" href="https://fonts.googleapis.com/css2?family=Arimo:wght@400;700&family=Inter:wght@300&display=swap">
<style>
  :root {
    --teal: #15799a;
    --page: #e8e8e8;
    --white: #ffffff;
    --ink: #2b2b2b;
    --photo-sky: #cfe0f3;
    --photo-light: #eef4fb;
  }
  * { margin: 0; padding: 0; box-sizing: border-box; }
  html, body {
    width: 1200px; height: 735px; overflow: hidden;
    background: var(--page);
    font-family: "Arimo", Arial, sans-serif;
  }
  .flyer {
    position: absolute; left: 335px; top: 103px;
    width: 530px; height: 530px; background: var(--white); overflow: hidden;
  }
  .voucher {
    position: absolute; left: 0; top: 0; width: 141px; height: 530px;
    background: var(--teal);
  }
  .voucher svg { display: block; }
  .services {
    position: absolute; left: 141px; top: 0; width: 161px; height: 383px;
  }
  .service-icon {
    position: absolute; left: 59px; width: 43px; height: 43px;
  }
  .service-label {
    position: absolute; left: 0; width: 161px; text-align: center;
    font-size: 11.5px; line-height: 13.6px; color: var(--ink); white-space: nowrap;
  }
  .service-rule {
    position: absolute; left: 16.5px; width: 129.5px; height: 1.5px;
    background: var(--teal);
  }
  .photo {
    position: absolute; left: 302px; top: 0; width: 228px; height: 383px;
    background:
      linear-gradient(160deg, transparent 55%, rgba(240,168,48,.55) 72%, rgba(232,86,58,.85) 88%),
      linear-gradient(180deg, var(--photo-sky) 0%, var(--photo-light) 55%, #f4efe9 100%);
  }
  .name-band {
    position: absolute; left: 141px; top: 383px; width: 389px; height: 33px;
    background: var(--teal); color: var(--white);
    font-size: 17.8px; line-height: 33px; text-align: center; white-space: nowrap;
  }
  .name-band strong { font-weight: 700; }
  .contact {
    position: absolute; font-size: 10.8px; line-height: 13.5px;
    color: #111; white-space: nowrap;
  }
  .contact-icon { position: absolute; width: 20px; height: 20px; }
  .contact-divider {
    position: absolute; left: 303.5px; top: 426px; width: 1.2px; height: 64px;
    background: var(--teal);
  }
  .brand-name {
    position: absolute; left: 322px; top: 435px; width: 180px;
    font-size: 11px; line-height: 13px; font-weight: 700; letter-spacing: .8px;
    color: var(--teal); white-space: nowrap;
  }
  .web-bar {
    position: absolute; left: 157px; top: 499px; width: 344px; height: 15px;
    background: var(--teal); color: var(--white);
    font-size: 12px; line-height: 15px; text-align: center;
  }
</style>
</head>
<body>
<main class="flyer">

  <section class="voucher" aria-label="Gutschein: 25 € Rabatt für Ihren Energieausweis">
    <svg width="141" height="530" viewBox="0 0 141 530">
      <rect x="17.5" y="15" width="106" height="498" fill="none" stroke="#fff" stroke-width="2"/>
      <line x1="26" y1="357" x2="113" y2="357" stroke="#fff" stroke-width="1.4"/>
      <g fill="#fff">
        <text transform="translate(65,298) rotate(-90)" font-family="Inter, Arial, sans-serif" font-weight="300" font-size="43" textLength="204" lengthAdjust="spacingAndGlyphs">FÜR IHREN</text>
        <text transform="translate(110,346) rotate(-90)" font-family="Arimo, Arial, sans-serif" font-weight="700" font-size="39" textLength="320" lengthAdjust="spacingAndGlyphs">ENERGIEAUSWEIS</text>
        <text transform="translate(81,495) rotate(-90)" font-family="Arimo, Arial, sans-serif" font-weight="700" font-size="70" textLength="127" lengthAdjust="spacingAndGlyphs">25 €</text>
        <text transform="translate(110,495) rotate(-90)" font-family="Arimo, Arial, sans-serif" font-weight="700" font-size="36" textLength="125" lengthAdjust="spacingAndGlyphs">RABATT</text>
      </g>
    </svg>
  </section>

  <section class="services">
    <svg class="service-icon" style="top:16.5px" viewBox="0 0 43 43" fill="none" stroke="#15799a" stroke-width="1.2">
      <circle cx="21.5" cy="21.5" r="20.5"/>
      <path d="M8 29 L32 12 L32 29 Z M14 27 L29 17 L29 27 Z"/>
    </svg>
    <p class="service-label" style="top:61px">Sanierungs- und<br>Modernisierungskonzepte</p>
    <div class="service-rule" style="top:97.5px"></div>

    <svg class="service-icon" style="top:110.5px" viewBox="0 0 43 43" fill="none" stroke="#15799a" stroke-width="1.2">
      <circle cx="21.5" cy="21.5" r="20.5"/>
      <rect x="11" y="11" width="21" height="21"/>
      <rect x="13.5" y="14" width="6" height="14"/>
      <path d="M22 14h8M22 17h8M22 20h8M22 23h8M22 26h8"/>
    </svg>
    <p class="service-label" style="top:157.5px">Erstellung von<br>Energieausweisen für<br>Vermietung und Verkauf</p>
    <div class="service-rule" style="top:207px"></div>

    <svg class="service-icon" style="top:220.5px" viewBox="0 0 43 43" fill="none" stroke="#15799a" stroke-width="1.2">
      <circle cx="21.5" cy="21.5" r="20.5"/>
      <circle cx="19" cy="21.5" r="11"/>
      <path d="M22 10.8 A11 11 0 0 1 22 32.2 M25 10.8 A11 11 0 0 1 25 32.2"/>
    </svg>
    <p class="service-label" style="top:265px">Fördermittelberatung</p>
    <div class="service-rule" style="top:289.5px"></div>

    <svg class="service-icon" style="top:302.5px" viewBox="0 0 43 43" fill="none" stroke="#15799a" stroke-width="1.2">
      <circle cx="21.5" cy="21.5" r="20.5"/>
      <path d="M24 8 L14 24 L21 24 L18 36 L29 19 L22 19 Z"/>
    </svg>
    <p class="service-label" style="top:347px">Energieberatung</p>
  </section>

  <div class="photo" role="img" aria-label="Foto: Modellhaus mit rotem Dach auf Bauplänen mit farbiger Energieeffizienzskala A bis G"></div>

  <div class="name-band">ENERGIEBERATUNG <strong>JONAS WENDLER</strong></div>

  <svg class="contact-icon" style="left:157px;top:436px" viewBox="0 0 20 20">
    <circle cx="10" cy="10" r="10" fill="#15799a"/>
    <path d="M10 15.5 C7 12 6 10.5 6 8.5 A4 4 0 0 1 14 8.5 C14 10.5 13 12 10 15.5 Z" fill="none" stroke="#fff" stroke-width="1.1"/>
    <circle cx="10" cy="8.6" r="1.4" fill="none" stroke="#fff" stroke-width="1"/>
  </svg>
  <p class="contact" style="left:183px;top:433px">Am Lindenhang 12<br>35690 Dillstadt</p>

  <svg class="contact-icon" style="left:157px;top:471px" viewBox="0 0 20 20">
    <circle cx="10" cy="10" r="10" fill="#15799a"/>
    <path d="M6.5 5 L8.5 5 L9.5 7.8 L8.3 9 C9 10.6 9.9 11.5 11.2 12 L12.4 10.8 L15 12 L15 14 C15 14.6 14.5 15 14 15 C9.6 14.7 5.5 10.6 5.2 6.2 C5.2 5.5 5.8 5 6.5 5 Z" fill="none" stroke="#fff" stroke-width="1.1"/>
  </svg>
  <p class="contact" style="left:183px;top:474px">+49 0151 47291836</p>

  <div class="contact-divider"></div>

  <p class="brand-name">ENERGIEBERATUNG<br>WENDLER</p>

  <svg class="contact-icon" style="left:316px;top:470px" viewBox="0 0 20 20">
    <circle cx="10" cy="10" r="10" fill="#15799a"/>
    <rect x="5" y="6.5" width="10" height="7" fill="none" stroke="#fff" stroke-width="1.1"/>
    <path d="M5 6.5 L10 10.5 L15 6.5" fill="none" stroke="#fff" stroke-width="1.1"/>
  </svg>
  <p class="contact" style="left:341px;top:474px">info@energieberatung-wendler.de</p>

  <div class="web-bar">www.energieberatung-wendler.de</div>
</main>
</body>
</html>
```